Breezy Burro Menu Design for new restaurant

Need a menu design for new restaurant- Fast Casual Taqueria. I have the files for our logo and menu already completed. Let me know what type of file your require and I can send it with regard to my logo. I want it to be easy to read but on a half page rack size type card, front and back. Simple and to the point but important to include the items listed with ingredients. Feel free to use icons for different categories.

Target Market(s)

Any one who loves tacos and margaritas...fun...festive...casual...

Font styles to use
Other font styles liked:
• lobster 1.3 and farmer round

Colors
3276b5
ec1f27
ffffff
85cae6
9bcb3c
fbed22

Requirements
Must have
• Designed for a half page, front and back (4.25 x 11). NO full size page menu. Easy to read. Not complicated. Use our logo. I need to be able to modify the menu from my end with out any special software.
Nice to have
• Fun~Festive~ color. Stick with our logo theme using our font lobster 1.3 and farmer round.
Should not have
• Full page format. Do not want stock food phots. Just graphics or icons.

```html
<!DOCTYPE html>
<html lang="en">
<head>
<meta charset="utf-8">
<title>Breezy Burro Menu</title>
<link href="https://fonts.googleapis.com/css2?family=Bebas+Neue&family=Lobster&family=Roboto+Condensed:wght@400&display=swap" rel="stylesheet">
<style>
  :root {
    --backdrop: #2b2321;
    --paper: #ffffff;
    --ink: #111111;
    --yellow: #fbed22;
    --red: #ec1f27;
    --frame: #1a1a1a;
    --art: #e6e6e6;
  }
  * { box-sizing: border-box; margin: 0; padding: 0; }
  html, body { width: 1200px; height: 799px; overflow: hidden; }
  body { background: var(--backdrop); position: relative; font-family: "Roboto Condensed", sans-serif; color: var(--ink); }

  .menu-card { position: absolute; top: 54px; width: 267px; height: 691px; background: var(--paper); }
  .menu-front { left: 429px; }
  .menu-back { left: 789px; }

  .card-frame { position: absolute; inset: 9px 7px 9px 7px; border: 1.5px solid var(--frame); }
  .brand-box { position: absolute; top: 0; left: 88px; width: 91px; height: 83px; background: var(--yellow);
    display: flex; align-items: center; justify-content: center; }
  .brand-name { font-family: "Lobster", cursive; color: var(--red); font-size: 17px; line-height: 1; text-align: center; }

  .site-url { position: absolute; left: 0; right: 0; top: 675px; text-align: center; }
  .site-url span { background: var(--paper); padding: 0 10px; font-size: 7px; letter-spacing: 2.6px; }

  .hero-art { position: absolute; left: 30px; top: 94px; width: 209px; height: 148px;
    background: radial-gradient(circle at 50% 60%, #cfcfcf 0%, var(--art) 55%, var(--paper) 75%); }

  .party-band { position: absolute; left: 0; top: 263px; width: 174px; height: 45px; background: var(--yellow); padding: 2px 0 0 12px; color: var(--red); }
  .party-band .kicker { font-family: "Bebas Neue", sans-serif; font-size: 15px; line-height: 14px; letter-spacing: .4px; }
  .party-band .script { font-family: "Lobster", cursive; font-size: 26px; line-height: 26px; }

  .menu-item { position: absolute; left: 12px; width: 230px; }
  .menu-back .menu-item { left: 14px; width: 240px; }
  .item-name { font-family: "Bebas Neue", sans-serif; font-size: 14px; line-height: 13px; letter-spacing: .2px; }
  .item-desc { font-size: 5.4px; line-height: 7.4px; }
  .bowl-item .item-desc { font-size: 6.4px; line-height: 8.4px; }

  .bowl-banner { position: absolute; left: 0; top: 579px; width: 162px; height: 18px; background: var(--red);
    clip-path: polygon(0 0, 100% 0, 94% 50%, 100% 100%, 0 100%); color: var(--paper);
    font-family: "Bebas Neue", sans-serif; font-size: 13px; line-height: 19px; padding-left: 12px; }
  .bowl-badge { position: absolute; left: 189px; top: 606px; }

  .section-tab { position: absolute; left: 0; width: 60px; height: 16px; background: var(--yellow);
    font-family: "Bebas Neue", sans-serif; font-size: 14px; line-height: 17px; padding-left: 14px; }
  .tab-tacos { top: 99px; }
  .tab-drinks { top: 483px; }
  .section-note { position: absolute; left: 15px; top: 125px; font-size: 5.4px; }
  .gf-note { position: absolute; left: 10px; top: 457px; font-size: 5.4px; line-height: 12px; }
  .gf-note .tag { background: var(--red); color: var(--paper); font-size: 6.2px; padding: 2px 2px; }

  .drink-line { position: absolute; left: 14px; font-family: "Bebas Neue", sans-serif; font-size: 11.5px; line-height: 12px; white-space: nowrap; }
  .beer-tag { position: absolute; left: 15px; top: 571px; background: var(--red); color: var(--paper); padding: 0 3px;
    font-family: "Bebas Neue", sans-serif; font-size: 9px; line-height: 12px; }
  .cocktail-art { position: absolute; left: 199px; top: 545px; width: 52px; height: 62px; }
</style>
</head>
<body>

<section class="menu-card menu-front">
  <div class="card-frame"></div>
  <div class="brand-box"><span class="brand-name">Breezy<br>Burro</span></div>
  <div class="hero-art" role="img" aria-label="Black and white illustration of a taco engulfed in flames with radiating lines"></div>

  <div class="party-band">
    <div class="kicker">Let's get this</div>
    <div class="script">Party Started</div>
  </div>

  <div class="menu-item" style="top:316px"><div class="item-name">Mexican Poke</div><div class="item-desc">fresh Ahi Tuna blended w/ spices &amp; ponzu on a bed of colored cabbage</div></div>
  <div class="menu-item" style="top:342px"><div class="item-name">Mermaid Tails</div><div class="item-desc">Shrimp Tempura beached on coconut slaw w/ sweet heat glaze, rice pearls,<br>fresh cilantro</div></div>
  <div class="menu-item" style="top:374px"><div class="item-name">Fiesta Nachos</div><div class="item-desc">crunchy tortilla chips layered w/ queso fresco, pickled vegetables, black beans,<br>tomatillo salsa, dry chile salsa &amp;cilantro. As flavorful as it is colorful!</div></div>
  <div class="menu-item" style="top:409px"><div class="item-name">Chorizo &amp; Queso</div><div class="item-desc">melted queso fresco w/ Chorizo crumbles, caramelized onions, cilantro</div></div>
  <div class="menu-item" style="top:435px"><div class="item-name">Elote</div><div class="item-desc">roasted corn sliced from the cob, chopped onions and poblano peppers<br>w/ cotija cheese, smoky homemade morita mayo &amp; Rojo Loco</div></div>
  <div class="menu-item" style="top:470px"><div class="item-name">Guacamole &amp; Chips</div><div class="item-desc">smooth blend of Haas avocados, jalapeño, red onions</div></div>
  <div class="menu-item" style="top:497px"><div class="item-name">Chips and Salsa</div><div class="item-desc">tortilla chips w/ choice of traditional rojo salsa or tomatillo verde</div></div>
  <div class="menu-item" style="top:525px"><div class="item-name">Queso and Chips</div><div class="item-desc">melted queso fresco &amp; crunchy tortilla chips</div></div>
  <div class="menu-item" style="top:553px"><div class="item-name">Rice &amp; Black Beans</div><div class="item-desc">traditional Mexican arroz verde &amp; black beans seasoned w/ epazote</div></div>

  <div class="bowl-banner">Make any Breezy Burro into a bowl</div>

  <div class="menu-item bowl-item" style="top:604px;width:175px"><div class="item-name">Ensalada</div><div class="item-desc">Chopped field greens, black beans, elote, avocado smash,<br>fresh cilantro &amp; queso fresco</div></div>
  <div class="menu-item bowl-item" style="top:639px;width:175px"><div class="item-name">Rice &amp; Beans</div><div class="item-desc">Traditional Mexican arroz verde, seasoned black beans &amp;<br>queso fresco</div></div>

  <svg class="bowl-badge" width="64" height="64" viewBox="0 0 64 64" aria-hidden="true">
    <circle cx="32" cy="32" r="30" fill="var(--paper)" stroke="var(--red)" stroke-width="3"/>
  </svg>

  <div class="site-url"><span>WWW.BREEZYBURRO-EATS.COM</span></div>
</section>

<section class="menu-card menu-back">
  <div class="card-frame"></div>
  <div class="brand-box"><span class="brand-name">Breezy<br>Burro</span></div>

  <div class="section-tab tab-tacos">Tacos</div>
  <div class="section-note">*All tacos finished Breezy Style with fresh cilantro, side of dry chile salsa &amp; lime wedges</div>

  <div class="menu-item" style="top:165px"><div class="item-name">Barbacoa</div><div class="item-desc">spiced Angus beef, cool creama, white diced onion, tomatillo-avocado sals</div></div>
  <div class="menu-item" style="top:190px"><div class="item-name">Al Pastor</div><div class="item-desc">spit-grilled Heritage Pork, diced white onion, charred pineapple, queso fresco</div></div>
  <div class="menu-item" style="top:216px"><div class="item-name">Carnitas</div><div class="item-desc">slow simmered Heritage Pork, avocado smash, pickled red onion, blistered<br>shishito peppers</div></div>
  <div class="menu-item" style="top:250px"><div class="item-name">Alabama Slamma</div><div class="item-desc">pulled smoked chicken, Alabama White Sauce, pickled cabbage, fried onions,<br>bacon blanket</div></div>
  <div class="menu-item" style="top:285px"><div class="item-name">Chick Next Door</div><div class="item-desc">grilled chicken breast, elote, avocado smash, queso fresco, salsa verde</div></div>
  <div class="menu-item" style="top:311px"><div class="item-name">Yinzer</div><div class="item-desc">grilled flat iron steak w/peppers &amp; onions, melted queso fresco, house jalapeño<br>salsa, chicharrónes</div></div>
  <div class="menu-item" style="top:345px"><div class="item-name">Beach Bum</div><div class="item-desc">maple fire roasted sweet potato, seasoned black beans, tropical slaw, toasted coconut</div></div>
  <div class="menu-item" style="top:371px"><div class="item-name">Island Time</div><div class="item-desc">battered avocado, sweet teriyaki glaze, charred pineapple, pickled red onion, queso fresco</div></div>
  <div class="menu-item" style="top:398px"><div class="item-name">Tropical Shrimp</div><div class="item-desc">Shrimp Tempura, avocado smash, tropical slaw, sweet heat creama, toasted coconut</div></div>
  <div class="menu-item" style="top:424px"><div class="item-name">Cabo Fish</div><div class="item-desc">beer battered Cod, pickled cabbage, spicy escabeche and smoky homemade morita mayo</div></div>

  <div class="gf-note">*only GF if on corn tortilla, filling is GF however... <span class="tag">try in a rice or ensalada bowl!</span></div>

  <div class="section-tab tab-drinks">Drinks</div>

  <div class="drink-line" style="top:509px">Tea- 20 oz...____</div>
  <div class="drink-line" style="top:523px">Soda Fountain 20 oz...____</div>
  <div class="drink-line" style="top:537px">Bottle Soda- See Selection</div>
  <div class="drink-line" style="top:551px">Draft Beer...16 oz...____ Pitcher...____</div>
  <div class="beer-tag">Bottle Beer Import/Domestic-See Selection</div>
  <div class="drink-line" style="top:590px">FZ Margarita 16 oz...____ Pitcher...____</div>
  <div class="drink-line" style="top:604px">Tap Margarita 16 oz...____ Pitcher...____</div>
  <div class="drink-line" style="top:618px">Sangria- 16 oz...____ Pitcher...____</div>
  <div class="drink-line" style="top:632px">Tequila Single Shot- Cheap...____ Standard...____ Premium...____</div>
  <div class="drink-line" style="top:646px">Tequila Double Shot -Cheap...____ Standard...____ Premium...____</div>

  <svg class="cocktail-art" viewBox="0 0 52 62" role="img" aria-label="Illustration of a cocktail glass with an umbrella on a yellow circle">
    <circle cx="26" cy="32" r="25" fill="var(--yellow)"/>
  </svg>

  <div class="site-url"><span>WWW.BREEZYBURRO-EATS.COM</span></div>
</section>

</body>
</html>
```